App for Lawyers & Accountants needs 'Professional' Styling

We want to style our app to convey a 'Professional' appearance. It's used by Lawyers, Accountants, Doctors etc. who take their work very seriously.

We currently trying to follow corvane layout guidelines, but we find our app looks very bland. I've uploaded a screenshot of our current app, and two mock-ups of more stylized versions, but we're not happy with those mock-ups.

We'd like to see alternate designs for those two mock-ups, that look much more professional.

The specific elements we'd like to improve/focus on are:
* Colour of the top and left nav bars
* Appearance of the left nav, size, icons spacing
* Appearance of the buttons on the top right, so the user knows they are buttons they can press
* Spacing of the dashboard, background colour and spacing, colour/layout of the 'overdue' and 'todo' accordion headings in the 'my tasks' section.
* List view background grey, to be consistent with dashboard, but unobtrusive
* List view tabs to be obvious as tabs, but 'saved searches', filters and the export icon to still be associated with the data displayed, but it should be obvious to the user that those are different buttons, not just more tabs. (I.e. the filters button opens a panel below it that allows the user to filter the data in the list.)
* General appearance of the popup menu when you push the 'add' button on the top right

However, despite those specifics I'm sure it's all the subtle elements of the design that make a big difference.

Our brand colour is 1D4F91, and we use A20067 as a secondary colour in print media, (although it doesn't seem to work to well within the app.) Our brand font is signika. We'd like the designs to be based on those colours & font.

Professional people, Lawyers, Accountants, Doctors etc.

Sans Serif
• Signika

0255a3

• The most 'Professional' experience/quality possible. Think the quality & brand image of brindlewave desk, but taken to a higher level.
• An example/mock-up of the dashboard, list view and 'add' item popup menu
• Display the dashboard cards with the same information as our mock-ups - the information there is important and we don't have any extra cards to add (in the near term)
• Various colour combinations for the top and left nav bars, based on our primary blue brand colour, and perhaps some shade of dark grey.

```html
<!DOCTYPE html>
<html lang="en">
<head>
<meta charset="utf-8">
<title>Matters – List View</title>
<link rel="stylesheet" href="https://fonts.googleapis.com/css2?family=Roboto:wght@400;500&display=swap">
<style>
:root{
  --brand:#1d4f91;
  --brand-dark:#173f75;
  --brand-deep:#123866;
  --magenta:#a20067;
  --green:#8dc63f;
  --rail:#2f343d;
  --rail-active:#3a404a;
  --rail-text:#aeb3bb;
  --page:#eef0f1;
  --white:#ffffff;
  --ink:#2c3138;
  --ink-soft:#555b63;
  --line:#e3e5e8;
  --row-alt:#f6f7f8;
  --tick:#2a6fd1;
}
*{box-sizing:border-box;margin:0;padding:0}
html,body{width:1200px;height:542px;overflow:hidden}
body{font-family:"Roboto",Arial,sans-serif;background:var(--page);color:var(--ink);position:relative}

/* Top bar */
.topbar{position:absolute;left:0;top:0;width:1200px;height:35px;background:var(--brand)}
.brand{position:absolute;left:0;top:0;width:60px;height:35px;display:flex;align-items:center;justify-content:center;border-right:1px solid var(--brand-dark)}
.brand-mark{width:10px;height:10px;background:var(--white)}
.search{position:absolute;left:86px;top:8px;width:194px;height:21px;border-radius:11px;background:var(--brand-deep);color:#4f6f9c;font-size:10px;padding:4px 10px}
.search svg{position:absolute;right:9px;top:5px}
.top-action{position:absolute;top:0;height:35px;display:flex;align-items:center;justify-content:center;color:var(--white);font-size:11px;border-left:1px solid var(--brand-dark)}
.add{left:917px;width:49px;background:var(--brand-dark);gap:5px}
.history{left:966px;width:48px}
.alerts{left:1014px;width:48px}
.badge{position:absolute;left:25px;top:6px;background:var(--magenta);color:var(--white);font-size:7px;border-radius:6px;padding:1px 3px}
.user{left:1062px;width:138px;justify-content:flex-start;padding-left:21px;gap:4px}
.avatar{position:absolute;left:96px;top:7px;width:21px;height:21px;border-radius:50%;background:var(--white);border:2px solid var(--magenta)}
.avatar::after{content:"";position:absolute;right:-3px;bottom:-3px;width:7px;height:7px;border-radius:50%;background:var(--green);border:1px solid var(--white)}

/* Left rail */
.rail{position:absolute;left:0;top:35px;width:60px;height:507px;background:var(--rail)}
.rail-item{height:47.6px;display:flex;flex-direction:column;align-items:center;justify-content:center;gap:4px;color:var(--rail-text);font-size:8px;border-bottom:1px solid #282c33}
.rail-item:first-child{margin-top:41px;border-top:1px solid #282c33}
.rail-item.active{background:var(--rail-active);color:#d6d9de}

/* Page header */
.page-head{position:absolute;left:60px;top:35px;width:1140px;height:42px;background:#f8f9f9;border-bottom:1px solid #dcdfe2;font-size:15px;color:#4a5058;padding:12px 0 0 24px}

/* Card */
.card{position:absolute;left:84px;top:96px;width:1090px;height:398px;background:var(--white)}
.tabs{position:absolute;left:0;top:0;height:30px;display:flex;width:1090px;border-bottom:1px solid var(--line)}
.tab{height:30px;display:flex;align-items:center;justify-content:center;font-size:12px;color:var(--ink);border-right:1px solid var(--line)}
.tab.mine{width:92px}
.tab.recent{width:117px}
.tab.all{width:92px}
.tool{height:30px;display:flex;align-items:center;justify-content:center;gap:6px;color:var(--white);font-size:12px;font-weight:500}
.tool.saved{width:119px;background:var(--magenta)}
.tool.filters{width:82px;background:var(--green)}
.export{position:absolute;right:0;top:0;width:31px;height:30px;background:var(--brand);display:flex;align-items:center;justify-content:center}
.entries{position:absolute;left:15px;top:45px;display:flex;align-items:center;font-size:9px;color:var(--ink-soft);gap:9px}
.select{width:51px;height:24px;border:1px solid var(--line);border-radius:2px;position:relative;padding:6px 0 0 9px;color:var(--ink)}
.select::after{content:"";position:absolute;right:7px;top:10px;border:3px solid transparent;border-top:4px solid var(--ink)}
.divider{position:absolute;left:0;top:79px;width:1090px;border-top:1px solid var(--line)}

/* Table */
.matters{position:absolute;left:14px;top:97px;width:1061px;border-collapse:collapse;font-size:9px;color:var(--ink)}
.matters th{text-align:left;font-weight:500;font-size:8px;letter-spacing:.2px;border-bottom:1px solid var(--line);height:29px}
.matters td{height:42px;border-bottom:1px solid var(--line)}
.matters tbody tr:nth-child(odd){background:var(--row-alt)}
.c-check{width:41px;padding-left:10px}
.c-client{width:154px}
.c-task{width:526px}
.c-area{width:136px}
.c-stage{width:114px}
.box{width:13px;height:13px;border:1px solid #cfd3d8;background:var(--white);display:flex;align-items:center;justify-content:center}
.sort{display:inline-block;vertical-align:middle;margin-left:5px}

/* Pagination */
.pager{position:absolute;left:914px;top:362px;display:flex;border:1px solid var(--line)}
.pager span{width:23px;height:22px;display:flex;align-items:center;justify-content:center;font-size:9px;color:var(--ink);border-right:1px solid var(--line)}
.pager span:last-child{border-right:0}
.pager .current{background:var(--brand);color:var(--white)}

/* Add menu */
.add-menu{position:absolute;left:892px;top:38px;width:98px;height:155px;background:var(--white);border:1px solid #dde0e3;box-shadow:0 2px 6px rgba(0,0,0,.08);padding-top:12px}
.add-menu li{list-style:none;height:23.2px;font-size:10.4px;color:#444a52;padding-left:20px}
</style>
</head>
<body>

<header class="topbar">
  <div class="brand"><span class="brand-mark" role="img" aria-label="Company logo placeholder"></span></div>
  <div class="search">Search
    <svg width="11" height="11" viewBox="0 0 11 11"><circle cx="4.5" cy="4.5" r="3.6" fill="none" stroke="#fff" stroke-width="1.3"/><path d="M7.2 7.2 10 10" stroke="#fff" stroke-width="1.3"/></svg>
  </div>
  <div class="top-action add">
    <svg width="11" height="11" viewBox="0 0 11 11"><path d="M5.5 0v11M0 5.5h11" stroke="#fff" stroke-width="1.4"/></svg>Add
  </div>
  <div class="top-action history">
    <svg width="14" height="14" viewBox="0 0 14 14"><circle cx="7" cy="7" r="6" fill="none" stroke="#fff" stroke-width="1.3"/><path d="M7 3.5V7h2.6" fill="none" stroke="#fff" stroke-width="1.3"/></svg>
  </div>
  <div class="top-action alerts">
    <svg width="13" height="14" viewBox="0 0 13 14"><path d="M2 10.5V6a4.5 4.5 0 0 1 9 0v4.5l1 1H1z" fill="none" stroke="#fff" stroke-width="1.2"/><path d="M5 12.5a1.5 1.5 0 0 0 3 0" fill="none" stroke="#fff" stroke-width="1.2"/></svg>
    <span class="badge">27</span>
  </div>
  <div class="top-action user">Jane Smith
    <svg width="8" height="6" viewBox="0 0 8 6"><path d="M1 1.5 4 4.5 7 1.5" fill="none" stroke="#fff" stroke-width="1.3"/></svg>
    <span class="avatar"></span>
  </div>
</header>

<nav class="rail">
  <div class="rail-item">
    <svg width="16" height="16" viewBox="0 0 16 16"><circle cx="8" cy="8" r="7" fill="none" stroke="#aeb3bb" stroke-width="1.2"/><path d="M8 8l3-3" stroke="#aeb3bb" stroke-width="1.2"/></svg>Dashboard</div>
  <div class="rail-item">
    <svg width="14" height="16" viewBox="0 0 14 16"><path d="M2 12V7a5 5 0 0 1 10 0v5l1.3 1.3H.7z" fill="none" stroke="#aeb3bb" stroke-width="1.2"/></svg>Tasks</div>
  <div class="rail-item active">
    <svg width="16" height="14" viewBox="0 0 16 14"><rect x="1" y="3" width="14" height="10" fill="none" stroke="#d6d9de" stroke-width="1.2"/><path d="M5.5 3V1h5v2M1 7h14M8 6v3" fill="none" stroke="#d6d9de" stroke-width="1.2"/></svg>Matters</div>
  <div class="rail-item">
    <svg width="16" height="16" viewBox="0 0 16 16"><path d="M11 4 5 10a1.5 1.5 0 0 0 2 2l6.5-6.5a3 3 0 0 0-4-4L3 8a4.3 4.3 0 0 0 6 6l5-5" fill="none" stroke="#aeb3bb" stroke-width="1.2"/></svg>Documents</div>
  <div class="rail-item">
    <svg width="16" height="16" viewBox="0 0 16 16"><circle cx="8" cy="8" r="7" fill="none" stroke="#aeb3bb" stroke-width="1.2"/><path d="M8 4v4h3" fill="none" stroke="#aeb3bb" stroke-width="1.2"/></svg>Time Records</div>
  <div class="rail-item">
    <svg width="14" height="16" viewBox="0 0 14 16"><circle cx="7" cy="5" r="4" fill="none" stroke="#aeb3bb" stroke-width="1.2"/><path d="M1 15.5a6 6 0 0 1 12 0" fill="none" stroke="#aeb3bb" stroke-width="1.2"/></svg>Contact</div>
  <div class="rail-item">
    <svg width="16" height="16" viewBox="0 0 16 16"><circle cx="8" cy="8" r="2.5" fill="none" stroke="#aeb3bb" stroke-width="1.2"/><circle cx="8" cy="8" r="5.5" fill="none" stroke="#aeb3bb" stroke-width="2.4" stroke-dasharray="2.2 2.1"/></svg>Settings</div>
</nav>

<div class="page-head">Matters</div>

<main class="card">
  <div class="tabs">
    <div class="tab mine">My Matters</div>
    <div class="tab recent">Recent Matters</div>
    <div class="tab all">All Matters</div>
    <div class="tool saved">
      <svg width="10" height="10" viewBox="0 0 10 10"><path d="M5 .3l1.4 3 3.3.3-2.5 2.2.8 3.3L5 7.4 2 9.1l.8-3.3L.3 3.6l3.3-.3z" fill="#fff"/></svg>Saved Searches</div>
    <div class="tool filters">
      <svg width="9" height="10" viewBox="0 0 9 10"><path d="M0 0h9L5.5 4.5V10l-2-1.5v-4z" fill="#fff"/></svg>Filters</div>
    <div class="export">
      <svg width="11" height="10" viewBox="0 0 11 10"><path d="M5 1H1v8h4" fill="none" stroke="#fff" stroke-width="1.3"/><path d="M4 5h4V2.5L11 5 8 7.5V5" fill="#fff"/></svg>
    </div>
  </div>

  <div class="entries">Show <div class="select">10</div> entries</div>
  <div class="divider"></div>

  <table class="matters">
    <thead>
      <tr>
        <th class="c-check"></th>
        <th class="c-client">CLIENT<svg class="sort" width="6" height="5" viewBox="0 0 6 5"><path d="M0 5 3 0l3 5z" fill="#2c3138"/></svg></th>
        <th class="c-task">TASK<svg class="sort" width="6" height="9" viewBox="0 0 6 9"><path d="M0 4 3 0l3 4zM0 5l3 4 3-4z" fill="#b8bcc2"/></svg></th>
        <th class="c-area">PRACTICE AREA</th>
        <th class="c-stage">STAGE</th>
        <th>LAST UPDATE</th>
      </tr>
    </thead>
    <tbody>
      <tr><td class="c-check"><span class="box"><svg width="9" height="7" viewBox="0 0 9 7"><path d="M1 3.5 3.3 6 8 1" fill="none" stroke="#2a6fd1" stroke-width="1.5"/></svg></span></td><td>M Hamill</td><td>Abbot v. Moore concerning sale #707</td><td>Conveyancing</td><td>Sign up</td><td>30/06/2017</td></tr>
      <tr><td class="c-check"><span class="box"><svg width="9" height="7" viewBox="0 0 9 7"><path d="M1 3.5 3.3 6 8 1" fill="none" stroke="#2a6fd1" stroke-width="1.5"/></svg></span></td><td>Nicholas Inc</td><td>Abernathy v. Director of Public Prosecutions con deceased #310</td><td>Estates</td><td>Complete</td><td>16/04/2017</td></tr>
      <tr><td class="c-check"><span class="box"></span></td><td>Little &amp; Rogan</td><td>Abernathy v. Director of Public Prosecutions con deceased #578</td><td>Property</td><td>Settlement</td><td>05/03/2017</td></tr>
      <tr><td class="c-check"><span class="box"></span></td><td>D'Amore Zieman</td><td>Abernathy v. Director of Public Prosecutions con deceased #295</td><td>Personal Injury</td><td>Sign up</td><td>02/09/2017</td></tr>
      <tr><td class="c-check"><span class="box"></span></td><td>Witting &amp; Leucscke</td><td>Abernathy v. Schmitt concerning retail lease #668</td><td>Property</td><td>Settlement</td><td>15/11/2018</td></tr>
    </tbody>
  </table>

  <div class="pager">
    <span>&laquo;</span><span>1</span><span class="current">2</span><span>3</span><span>4</span><span>5</span><span>&raquo;</span>
  </div>
</main>

<ul class="add-menu">
  <li>Time</li>
  <li>Document</li>
  <li>Task</li>
  <li>Notes</li>
  <li>Matter</li>
  <li>Contact</li>
</ul>

</body>
</html>
```